New Website for novelty yarn producer

We need a new website for our company, Tarvek. We make highly tailored yarns for weavers worldwide. This year marks our 40th anniversary and we want to evolve our image and identity.

Our temporary website can be found at:
www.tarvekyarns.com

Our only concern in that throughout the website the protagonist must be our client, we make their creations possible and are highly adaptable both during the ideation process of the yarn as well as in the production. This is at the core of the way we do business and is summarised within the concept of FPM (Fluid Partner Method).

Industry/Entity Type

Textile

Number of Pages Required

1 page

Colors
9bcb3c

Requirements
Must have
• Fluid Partner Method (FPM) - can be found on or current website www.tarvekyarns.com

```html
<!DOCTYPE html>
<html lang="en">
<head>
<meta charset="utf-8">
<title>Tarvek – Novelty Yarn Solutions</title>
<link rel="stylesheet" href="https://fonts.googleapis.com/css2?family=Josefin+Sans:wght@400;600;700&family=Montserrat:wght@500;600;700&family=Open+Sans:wght@400;600&display=swap">
<style>
:root{
  --ink:#111111;
  --text:#222222;
  --muted:#8a8a8a;
  --soft:#a3a3a3;
  --green:#9bcb3c;
  --paper:#ffffff;
  --footer:#1f1f1f;
  --line:#111111;
}
*{margin:0;padding:0;box-sizing:border-box}
html,body{width:1200px;height:2296px;overflow:hidden;background:var(--paper)}
body{position:relative;font-family:"Open Sans",Arial,sans-serif;color:var(--text)}
.abs{position:absolute}

/* header */
.brand{left:164px;top:22px;font-family:"Josefin Sans",sans-serif;font-weight:700;font-size:56px;letter-spacing:2px;color:var(--ink);line-height:1}
.main-nav{left:475px;top:43px;width:565px;display:flex;justify-content:space-between;white-space:nowrap;font-family:"Montserrat",sans-serif;font-weight:600;font-size:10px;letter-spacing:.2px;color:var(--ink)}
.search-icon{left:1075px;top:40px}
.side-contact{left:1076px;top:107px;writing-mode:vertical-rl;font-family:"Montserrat",sans-serif;font-weight:700;font-size:10px;letter-spacing:.8px;color:var(--ink)}

/* hero */
.hero-machine{left:0;top:102px;width:519px;height:516px;background:linear-gradient(135deg,#5a6470 0%,#9aa3ad 40%,#3f4d63 70%,#6f7a86 100%)}
.hero-yarn{left:519px;top:102px;width:519px;height:516px;background:radial-gradient(circle at 65% 45%,#efe9df 0%,#d9cfc0 45%,#c9bba7 100%)}
.hero-badge{left:347px;top:245px}
.hero-tag{right:681px;background:var(--ink);color:#fff;font-family:"Josefin Sans",sans-serif;font-weight:600;font-variant:small-caps;white-space:nowrap;padding:0 10px;display:flex;align-items:center;line-height:1}
.hero-tag.one{top:363px;height:38px;font-size:23px}
.hero-tag.two{top:404px;height:37px;font-size:21px;letter-spacing:.5px}
.slider-controls{left:961px;top:638px;display:flex;gap:30px;font-family:"Montserrat",sans-serif;font-weight:600;font-size:10px;color:var(--ink)}

/* section labels */
.rule{height:2px;background:var(--line)}
.label{background:var(--ink);color:#fff;font-family:"Josefin Sans",sans-serif;font-weight:600;font-variant:small-caps;font-size:16px;letter-spacing:.4px;line-height:1;display:flex;align-items:center;justify-content:center;white-space:nowrap;padding:0 16px}

/* values */
.value{width:260px}
.value-head{display:flex;align-items:center;gap:14px;height:44px}
.value-title{font-family:"Montserrat",sans-serif;font-weight:600;font-size:12px;color:var(--ink)}
.value-text{margin-top:14px;font-size:11px;line-height:17px;color:var(--muted)}

/* approach */
.section-title{font-family:"Josefin Sans",sans-serif;font-weight:700;font-variant:small-caps;font-size:19px;letter-spacing:.6px;color:var(--ink)}
.approach-photo-threads{left:548px;top:1067px;width:491px;height:295px;background:linear-gradient(120deg,#e8e4dc 0%,#8fcbc0 22%,#2e8fb8 38%,#c9d641 52%,#e6602a 68%,#c7273f 82%,#f0e6da 100%)}
.approach-photo-cones{left:161px;top:1364px;width:364px;height:356px;background:radial-gradient(circle at 40% 55%,#c9643a 0%,#6f5a4d 35%,#3f4152 70%,#2a2d36 100%)}
.sub-title{font-family:"Montserrat",sans-serif;font-weight:600;font-size:12.5px;color:var(--ink)}
.body-copy{font-size:11px;line-height:20px;color:var(--muted)}
.approach-lead{left:161px;top:1246px;width:335px}
.approach-lead .body-copy{margin-top:6px}
.approach-detail{left:570px;top:1434px;width:468px;text-align:right}
.green-head{font-family:"Montserrat",sans-serif;font-weight:600;font-size:12px;color:var(--green)}
.approach-detail .sub-title{font-size:11.5px;margin-top:6px}
.approach-detail .body-copy{margin-top:6px}
.btn-outline{left:908px;top:1632px;width:130px;height:33px;border:1.5px solid var(--ink);font-family:"Montserrat",sans-serif;font-weight:600;font-size:12px;color:var(--ink);display:flex;align-items:center;justify-content:center}

/* team */
.portrait{width:191px;height:237px;top:1789px;background:linear-gradient(180deg,#c7c7c7 0%,#bdbdbd 55%,#8b8f98 100%)}
.portrait.first{left:161px}
.portrait.second{left:360px}
.team-panel{left:520px;top:1875px;width:680px;height:180px;background:var(--paper)}
.founder-name{top:2046px;font-family:"Montserrat",sans-serif;font-weight:600;font-size:13px;color:var(--ink);width:191px;text-align:center}
.member{top:1920px;width:170px}
.member-name{font-family:"Montserrat",sans-serif;font-weight:600;font-size:12px;color:var(--ink)}
.member-role{margin-top:12px;font-size:11.5px;line-height:14px;color:var(--soft)}
.team-arrows{left:550px;top:1995px;display:flex;gap:16px}

/* footer */
.site-footer{left:161px;top:2140px;width:1039px;height:156px;background:var(--footer);color:#fff}
.footer-title{left:29px;top:29px;font-family:"Montserrat",sans-serif;font-weight:700;font-size:12px}
.footer-legal{left:29px;top:55px;font-size:9.5px;line-height:13.5px;color:#cfcfcf}
.footer-nav{left:480px;top:34px;list-style:none;font-family:"Montserrat",sans-serif;font-weight:700;font-size:9.5px;line-height:24px}
.footer-brand{left:722px;top:32px;font-family:"Josefin Sans",sans-serif;font-weight:700;font-size:40px;letter-spacing:2px;line-height:1;color:#fff}
.footer-copy{left:656px;top:112px;font-family:"Montserrat",sans-serif;font-weight:600;font-size:9.5px;color:#fff}
</style>
</head>
<body>

<header>
  <div class="abs brand">TARVEK</div>
  <nav class="abs main-nav">
    <span>HOME</span><span>ABOUT US</span><span>FLUID PARTNER METHOD</span><span>HERITAGE</span><span>TEAM</span><span>BLOGS</span><span>CONTACT</span>
  </nav>
  <svg class="abs search-icon" width="18" height="18" viewBox="0 0 18 18"><circle cx="7" cy="7" r="5.5" fill="none" stroke="#111" stroke-width="2"/><line x1="11" y1="11" x2="16.5" y2="16.5" stroke="#111" stroke-width="2.2"/></svg>
  <div class="abs side-contact">CONTACT US</div>
</header>

<section class="hero">
  <div class="abs hero-machine" role="img" aria-label="Weaving machine with rows of white and blue yarn bobbins"></div>
  <div class="abs hero-yarn" role="img" aria-label="Balls of cream, beige and magenta knitting yarn on a table"></div>
  <svg class="abs hero-badge" width="86" height="86" viewBox="0 0 86 86" aria-hidden="true"><circle cx="43" cy="43" r="40" fill="none" stroke="#fff" stroke-width="2"/></svg>
  <div class="abs hero-tag one">Tailored Weaving Solutions</div>
  <div class="abs hero-tag two">Make Since 40th Year</div>
  <div class="abs slider-controls"><span>PREV</span><span>NEXT</span></div>
</section>

<section class="values">
  <div class="abs rule" style="left:1038px;top:700px;width:162px"></div>
  <div class="abs label" style="right:162px;top:701px;height:31px">Novelty Yarn Solution</div>

  <div class="abs value" style="left:161px;top:784px">
    <div class="value-head">
      <svg width="42" height="42" viewBox="0 0 42 42"><circle cx="21" cy="8" r="5" fill="#111"/><path d="M13 26v-7a3 3 0 0 1 3-3h10a3 3 0 0 1 3 3v7z" fill="#111"/><path d="M3 22l8 12h20l8-12" fill="none" stroke="#111" stroke-width="2.5" stroke-linejoin="round"/><path d="M11 34l-2 5M31 34l2 5" stroke="#111" stroke-width="2.5"/></svg>
      <span class="value-title">EXPERIENCE</span>
    </div>
    <p class="value-text">Over the years the company has gained the knowl-edge and skills that define the superiority of our product and the rigor of our work ethic</p>
  </div>

  <div class="abs value" style="left:478px;top:784px">
    <div class="value-head">
      <svg width="42" height="42" viewBox="0 0 42 42"><path d="M21 9a10 10 0 0 0-6 18v5h12v-5a10 10 0 0 0-6-18z" fill="#111"/><rect x="16" y="34" width="10" height="3" fill="#111"/><g stroke="#111" stroke-width="2"><line x1="21" y1="1" x2="21" y2="5"/><line x1="7" y1="7" x2="10" y2="10"/><line x1="35" y1="7" x2="32" y2="10"/><line x1="2" y1="19" x2="6" y2="19"/><line x1="36" y1="19" x2="40" y2="19"/></g></svg>
      <span class="value-title">CREATIVITY</span>
    </div>
    <p class="value-text">Our belief is that the key to our clients' success is a combination of innovation, creativity and quality. We strive to adapt and re-imagine</p>
  </div>

  <div class="abs value" style="left:796px;top:784px">
    <div class="value-head">
      <svg width="58" height="42" viewBox="0 0 58 42"><path d="M2 12l10-6 8 4M56 12l-10-6-12 6-8 7a3 3 0 0 0 4 4l8-5 12 11" fill="none" stroke="#111" stroke-width="2.5" stroke-linejoin="round"/><path d="M6 22l12 12a3 3 0 0 0 4-4M16 28l6 6a3 3 0 0 0 4-4M22 26l6 6a3 3 0 0 0 4-4" fill="none" stroke="#111" stroke-width="2.5" stroke-linecap="round"/></svg>
      <span class="value-title">PROFESSIONALITY</span>
    </div>
    <p class="value-text">We are a family business at the core. Our company is run with the same values as the Varelli family: respect, determination and commitment.</p>
  </div>
</section>

<section class="approach">
  <div class="abs rule" style="left:0;top:968px;width:161px"></div>
  <div class="abs label" style="left:161px;top:969px;height:32px">Flexible At The Core</div>

  <h2 class="abs section-title" style="left:161px;top:1064px">Fluid Partner Method</h2>
  <div class="abs approach-photo-threads" role="img" aria-label="Colourful woven yarn strands laid side by side"></div>

  <div class="abs approach-lead">
    <h3 class="sub-title">Production built around you</h3>
    <p class="body-copy">Versatility and flexibility both in development and production are key in delivering a custom solution capable of giving life to your products.</p>
  </div>

  <div class="abs approach-photo-cones" role="img" aria-label="Yarn cones with coloured plastic cores seen from above"></div>

  <div class="abs approach-detail">
    <h3 class="green-head">TNYS Fluid Partner Method</h3>
    <p class="sub-title">Your Tailored Clothes Experience :</p>
    <p class="body-copy">We believe that the key to delivering a yarn that exceeds our client's expectation is to work together with weavers from step one, starting from the desired end product and working backwards. This allows us to develop the product that our weavers need,rather than having weavers adapt to the supplied raw materials.<br>Our Fluid Partner Method consists achieving maximum flexibility both in development and production.</p>
  </div>
  <div class="abs btn-outline">Find Out More</div>
</section>

<section class="team">
  <div class="abs portrait first" role="img" aria-label="Portrait of founder Ilaria Venturini"></div>
  <div class="abs portrait second" role="img" aria-label="Portrait of founder Sergio Varelli"></div>
  <div class="abs rule" style="left:802px;top:1842px;width:398px"></div>
  <div class="abs team-panel"></div>
  <div class="abs label" style="left:551px;top:1843px;height:32px">Founders &amp; Operational team</div>

  <div class="abs founder-name" style="left:161px">Ilaria Venturini</div>
  <div class="abs founder-name" style="left:360px">Sergio Varelli</div>

  <div class="abs member" style="left:551px"><div class="member-name">Marco Delfini</div><div class="member-role">Head Of Sales</div></div>
  <div class="abs member" style="left:693px"><div class="member-name">Paola Rinaldi</div><div class="member-role">Head Of Administration<br>&amp; Control</div></div>
  <div class="abs member" style="left:888px"><div class="member-name">Franco Bellotti</div><div class="member-role">Sales &amp; Head Of Technical<br>Assistance</div></div>

  <div class="abs team-arrows">
    <svg width="14" height="16" viewBox="0 0 14 16"><path d="M10 2L4 8l6 6" fill="none" stroke="#111" stroke-width="2"/></svg>
    <svg width="14" height="16" viewBox="0 0 14 16"><path d="M4 2l6 6-6 6" fill="none" stroke="#111" stroke-width="2"/></svg>
  </div>
</section>

<footer class="abs site-footer">
  <div class="abs footer-title">Tarvek Novelty Yarn Solutions</div>
  <div class="abs footer-legal">Orvam s.r.l<br>Via dei Tessitori 14 - 50100 Corvane - Italy - Tel. 0500 11223 r.a. - Fax 0500 445566<br>R.E.A CV 481920- Reg. Imp. CV 04417730512<br>P. IVA 00920300418 - Cod. Fisc. 04417730512<br>Capitale sociale € 91. 541, 99 int. ver.</div>
  <ul class="abs footer-nav"><li>HOME</li><li>ABOUT US</li><li>FLUID PARTNER METHOD</li><li>MORE</li></ul>
  <div class="abs footer-brand">TARVEK</div>
  <div class="abs footer-copy">© Copyright 2018 Tarvek Novelty Yarn Solution.</div>
</footer>

</body>
</html>
```